Bootstrap site for Cloud Services company

Hi,

First I'd like you to submit you design of the homepage. If you are the winner, I'll get you do design the rest and code it up in HTML, CSS etc using bootstrap.

Why bootstrap? This will probably mean
that you understand the fundamentals of CSS and know how to
make a good-looking website. Also should mean that you can throw
together this site relatively easily so you can focus on the design
work. I'll need some icons and banner style images done.

There's no server-side coding involved, and there's also no content to write, just put placemarker text wherever appropriate. You must be familiar with bootstrap.

Our business sells Varnel Suite for Business and IT support services.

The icon for our business is attached.

Basically I want you to go by the design of this site
http://lnk.example-short.test/kQ7r

However, don't just copy it. I want it to be of a similar layout and
style, but be creative.

I like the simplicity and how it's easy to follow visually.

Just submit the homepage, and if you're successful, I'll get you to
design the rest of the pages for me and code up the pages.

Thanks!

Target Market(s)

We are marketing towards businesses that need their IT managed for them.

Industry/Entity Type

Business

Requirements
Must have
• I like how clean and nice the roboto font is, but it's up to you.

You're welcome to take inspiration from the 'Varnel Pulse' layout and design. Nice use of white space and layout.

Menu headings at the top are as follows:
Support | Deployment | Training | Development | Contact Us |
About

Home page:

In a similar style of the referenced webpage http://lnk.example-short.test/kQ7r, I'd
like a single banner that says "Brisbane's leading Varnel Suite
specialists". In the banner have a computer screen or laptop and a
tablet or smartphone with some 'varnel suite for business' style of
logos coming out of it be creative with some nice design.

Under that, 3 square (or something) icons.
Save Money | Collaborate | Grow
just put some placemarker text in it in a similar fashion to the
reference site.

Just throw some other things in there to fill it up a bit.
Should not have
• http://lnk.example-short.test/kQ7r
I don't want the scrolling banner with the site above, static is fine.

I don't like how when the menu is moused-over, the whole page
moves down.

No stock photos of 'successful business people' or 'very attractive
telephone operator waiting to take your call' :)

```html
<!DOCTYPE html>
<html lang="en">
<head>
<meta charset="utf-8">
<title>Skyvane – Varnel Suite Specialists</title>
<link rel="stylesheet" href="https://fonts.googleapis.com/css2?family=PT+Sans+Narrow:wght@400;700&family=PT+Sans:wght@400;700&display=swap">
<style>
:root{
  --blue:#3a85bb;
  --brand:#1d8ed8;
  --nav:#2b2d2f;
  --red:#f2473f;
  --yellow:#f7c531;
  --teal:#5cc5c4;
  --ink:#333;
  --muted:#555;
  --line:#e2e2e2;
  --link:#4fb8c9;
  --caption:rgba(40,44,48,.84);
}
*{box-sizing:border-box;margin:0;padding:0}
html,body{width:1200px;height:1166px;overflow:hidden}
body{font-family:"PT Sans Narrow",sans-serif;color:var(--ink);background:#fff;position:relative}
.top-strip{position:absolute;left:0;top:0;width:1200px;height:5px;background:var(--blue)}
.site-header{position:absolute;top:5px;left:0;width:1200px;height:82px}
.brand{position:absolute;left:171px;top:20px;display:flex;align-items:center;gap:12px}
.brand-mark{width:38px;height:38px;border-radius:50%;background:var(--brand)}
.brand-name{font-family:"PT Sans",sans-serif;font-size:44px;font-weight:400;color:var(--brand);line-height:1}
.account{position:absolute;top:23px;height:34px;border:1px solid #e4e4e4;background:linear-gradient(#fff,#f4f4f4);box-shadow:0 1px 3px rgba(0,0,0,.08);font-size:14px;letter-spacing:1px;display:flex;align-items:center;justify-content:center}
.account.register{left:798px;width:116px;color:var(--brand)}
.account.login{left:932px;width:97px;color:var(--red)}
.main-nav{position:absolute;top:87px;left:0;width:1200px;height:41px;background:var(--nav)}
.main-nav ul{list-style:none;position:absolute;left:176px;width:848px;top:0;height:41px;display:flex;justify-content:space-between;align-items:center}
.main-nav li{color:#fff;font-size:15px;letter-spacing:1.2px}
.hero{position:absolute;top:128px;left:0;width:1200px;height:319px;background:var(--blue)}
.hero-art{position:absolute;left:171px;top:15px;width:858px;height:285px;background:linear-gradient(90deg,#bfe3f8 0%,#a6d8f5 45%,#8ccaf0 100%);box-shadow:0 10px 18px -8px rgba(0,0,0,.45)}
.hero-caption{position:absolute;right:207px;top:108px;padding:12px 14px 14px 14px;background:var(--caption);border-top:8px solid rgba(40,44,48,.5);color:#fff;font-size:26px;line-height:31px;letter-spacing:1px;white-space:pre;text-align:left}
.cta{position:absolute;left:171px;top:471px;width:858px;height:73px;border:1px solid var(--line);background:#fafafa}
.cta h2{position:absolute;left:15px;top:13px;font-size:18.3px;font-weight:700;letter-spacing:.8px;color:#333;white-space:nowrap}
.cta p{position:absolute;left:15px;top:39px;font-size:11.6px;letter-spacing:.8px;color:#444;white-space:nowrap}
.cta-button{position:absolute;left:671px;top:16px;width:172px;height:37px;background:var(--red);color:#a8231d;font-size:15px;font-weight:700;letter-spacing:1px;display:flex;align-items:center;justify-content:center}
.section-title{position:absolute;left:186px;top:568px;font-size:17px;font-weight:700;letter-spacing:1px}
.features{position:absolute;left:171px;top:601px;width:858px;border-top:1px solid var(--line)}
.feature-row{display:flex;border-bottom:1px solid var(--line);height:145px}
.feature{position:relative;padding:7px 0 0 4px;height:137px;margin-top:6px}
.feature+.feature{border-left:1px solid var(--line)}
.feature:nth-child(1){width:281px}
.feature:nth-child(2){width:285px;padding-left:14px}
.feature:nth-child(3){width:292px;padding-left:10px}
.feature-head{display:flex;align-items:center;gap:12px;height:34px}
.icon{width:34px;height:34px;border-radius:50%;display:flex;align-items:center;justify-content:center}
.icon.red{background:var(--red)}.icon.yellow{background:var(--yellow)}.icon.teal{background:var(--teal)}
.feature h3{font-size:18px;font-weight:700;letter-spacing:1px;color:#333}
.feature p{margin-top:9px;font-size:13.6px;line-height:18.8px;color:var(--muted);width:272px}
.lower{position:absolute;left:171px;top:928px;width:858px;height:140px}
.lower-art{position:absolute;left:0;top:0;width:264px;height:138px;border:1px solid var(--line);box-shadow:0 1px 3px rgba(0,0,0,.1);background:#fff;padding:8px}
.lower-art div{width:100%;height:100%;background:linear-gradient(135deg,#f6c54a 0%,#ef5a4a 35%,#3b9fe0 70%,#5ac3a6 100%)}
.lower h2{position:absolute;left:294px;top:7px;font-size:17px;font-weight:700;letter-spacing:1px}
.lower p{position:absolute;left:294px;top:36px;width:560px;font-size:13.6px;line-height:24px;color:var(--muted)}
.read-more{position:absolute;left:294px;top:117px;font-size:12.5px;color:var(--link);letter-spacing:.5px}
.read-more::after{content:"";display:inline-block;margin-left:6px;border-left:4px solid var(--link);border-top:3.5px solid transparent;border-bottom:3.5px solid transparent}
.site-footer{position:absolute;left:0;top:1110px;width:1200px;height:56px;background:var(--blue)}
.site-footer .copy{position:absolute;left:173px;top:21px;font-size:10px;letter-spacing:.8px;color:#1d2a36}
.site-footer ul{list-style:none;position:absolute;right:171px;top:21px;display:flex;gap:14px;font-size:10px;letter-spacing:.8px;color:#1d2a36}
.site-footer li.active{color:var(--red)}
</style>
</head>
<body>
<div class="top-strip"></div>
<header class="site-header">
  <div class="brand"><span class="brand-mark"></span><span class="brand-name">Skyvane</span></div>
  <div class="account register">Register</div>
  <div class="account login">Login</div>
</header>
<nav class="main-nav">
  <ul><li>Home</li><li>About</li><li>Support</li><li>Deployment</li><li>Training</li><li>Development</li><li>Contact Us</li></ul>
</nav>
<section class="hero">
  <div class="hero-art" role="img" aria-label="Tablets in front and back view beside a laptop surrounded by colourful round app icons on a light blue background"></div>
  <div class="hero-caption">Brisbane's leading Varnel Suite
specialists</div>
</section>
<section class="cta">
  <h2>Lorem ipsum dolor sit amet consectetur adipiscing eliterreing</h2>
  <p>Integer rutrum nunc eu dui rutrum vel cursus purus fermentum. Duis mattis odio id erat vestibulum bibendum elenrotte eke</p>
  <div class="cta-button">Get Started</div>
</section>
<h2 class="section-title">Features &amp; Benefits</h2>
<section class="features">
  <div class="feature-row">
    <div class="feature">
      <div class="feature-head"><span class="icon red"><svg width="20" height="14" viewBox="0 0 20 14" fill="#fff"><circle cx="10" cy="4" r="3"/><circle cx="4" cy="5" r="2.3"/><circle cx="16" cy="5" r="2.3"/><path d="M4 14c0-4 3-6 6-6s6 2 6 6z"/><path d="M0 13c0-3 2-5 4-5 1 0 2 .3 2 .6-1 1-2 3-2 4.4z"/><path d="M20 13c0-3-2-5-4-5-1 0-2 .3-2 .6 1 1 2 3 2 4.4z"/></svg></span><h3>Collaborate</h3></div>
      <p>Fusce egestas luctus lacus vitae hendrerit. Morbi vitae nibh erat, non aliquet diam. Curabitur odio mauris, suscipit non blandit iaculis, tempor quis velit. Sed consequat justo et massa.</p>
    </div>
    <div class="feature">
      <div class="feature-head"><span class="icon yellow"><svg width="18" height="16" viewBox="0 0 18 16" fill="none" stroke="#fff" stroke-width="1.6"><path d="M1 1v14h16"/><path d="M3 12l4-4 3 2 6-6"/></svg></span><h3>Grow</h3></div>
      <p>Fusce egestas luctus lacus vitae hendrerit. Morbi vitae nibh erat, non aliquet diam. Curabitur odio mauris, suscipit non blandit iaculis, tempor quis velit. Sed consequat justo et massa.</p>
    </div>
    <div class="feature">
      <div class="feature-head"><span class="icon teal"><svg width="18" height="18" viewBox="0 0 18 18" fill="none" stroke="#fff" stroke-width="1.6"><ellipse cx="7" cy="5" rx="5" ry="2.5"/><path d="M2 5v6c0 1.4 2.2 2.5 5 2.5"/><circle cx="12" cy="12" r="4.5"/></svg></span><h3>Save Money</h3></div>
      <p>Fusce egestas luctus lacus vitae hendrerit. Morbi vitae nibh erat, non aliquet diam. Curabitur odio mauris, suscipit non blandit iaculis, tempor quis velit. Sed consequat justo et massa.</p>
    </div>
  </div>
  <div class="feature-row">
    <div class="feature">
      <div class="feature-head"><span class="icon red"><svg width="18" height="13" viewBox="0 0 18 13" fill="none" stroke="#fff" stroke-width="1.6"><rect x="1" y="1" width="16" height="11"/><path d="M1 1l8 6 8-6"/></svg></span><h3>Communiation</h3></div>
      <p>Fusce egestas luctus lacus vitae hendrerit. Morbi vitae nibh erat, non aliquet diam. Curabitur odio mauris, suscipit non blandit iaculis, tempor quis velit. Sed consequat justo et massa.</p>
    </div>
    <div class="feature">
      <div class="feature-head"><span class="icon yellow"><svg width="18" height="18" viewBox="0 0 18 18" fill="none" stroke="#fff" stroke-width="1.6"><circle cx="9" cy="9" r="7.5"/><path d="M4 5c2 1 3 0 4 2s-1 3 0 4 2 0 2 3M12 3c0 2 2 2 3 3"/></svg></span><h3>International</h3></div>
      <p>Fusce egestas luctus lacus vitae hendrerit. Morbi vitae nibh erat, non aliquet diam. Curabitur odio mauris, suscipit non blandit iaculis, tempor quis velit. Sed consequat justo et massa.</p>
    </div>
    <div class="feature">
      <div class="feature-head"><span class="icon teal"><svg width="18" height="16" viewBox="0 0 18 16" fill="#fff"><rect x="1" y="11" width="16" height="4"/><rect x="4" y="7" width="11" height="3"/><rect x="7" y="3" width="8" height="3"/><rect x="10" y="0" width="5" height="2"/></svg></span><h3>Simple Steps</h3></div>
      <p>Fusce egestas luctus lacus vitae hendrerit. Morbi vitae nibh erat, non aliquet diam. Curabitur odio mauris, suscipit non blandit iaculis, tempor quis velit. Sed consequat justo et massa.</p>
    </div>
  </div>
</section>
<section class="lower">
  <div class="lower-art"><div role="img" aria-label="Laptop with a question mark on screen surrounded by colourful round service icons"></div></div>
  <h2>Lower Content Headline</h2>
  <p>Vestibulum non consectetur urna. Ut non quam quam. Nam congue rutrum leo, vel vulputate nibh mollis vel. Cras eleifend dui eget lectus vehicula eu ornare nunc sodales. Pellentesque habitant morbi tristique senectus et netus et malesuada fames ac turpis egestas. Cras luctus, turpis et semper rhoncus,</p>
  <span class="read-more">read more</span>
</section>
<footer class="site-footer">
  <div class="copy">Copyright © 2012 All rights reserved</div>
  <ul><li class="active">Home</li><li>About</li><li>Support</li><li>Development</li><li>Contact</li></ul>
</footer>
</body>
</html>
```